Supplement label for Brain health

I need a design for a supplement this supplement is a brain boost supplement.

The Name is Kelp Vantor.

I have attached other labels I like. This is for 50 plus demographic so the lettering needs to be easy to read and stand out. I have attached a dummy label template that once the winner is choosen then they will get the real supplement facts etc.

Clean desgin easy to read.

This file must be finished in AI format.

Target Market(s)

50 plus 70 percent female 30 percent male

Industry/Entity Type

Supplement

Font styles to use
Other font styles liked:
• Myrid pro maybe

Requirements
Must have
• easy to read text so no colors that hide text or hard to read.

```html
<!DOCTYPE html>
<html lang="en">
<head>
<meta charset="utf-8">
<title>Kelp Vantor – Brain Boost Supplement Label</title>
<link rel="stylesheet" href="https://fonts.googleapis.com/css2?family=Montserrat:wght@600&family=Open+Sans:wght@400;600&family=Arimo:wght@400;700&display=swap">
<style>
  :root{
    --blue:#3a9fe8;
    --blue-light:#8fd0f7;
    --orange:#e8830f;
    --navy:#152f7c;
    --grey:#7a7a7a;
    --ink:#222;
    --white:#fff;
  }
  *{box-sizing:border-box;margin:0;padding:0}
  html,body{width:1200px;height:427px;overflow:hidden;background:var(--white)}
  .label{position:relative;width:1200px;height:427px;overflow:hidden;background:var(--white);font-family:"Arimo",Arial,sans-serif;color:var(--navy)}

  /* left column */
  .directions{position:absolute;left:12px;top:24px;width:248px;font-size:8.6px;line-height:1.25}
  .directions p{margin-bottom:9px}
  .directions b{font-weight:700}
  .fda-note{position:absolute;left:14px;top:296px;width:242px;border:2px solid var(--navy);padding:3px 5px;font-size:7.6px;font-weight:700;line-height:1.2}
  .distributor{position:absolute;left:16px;top:352px;font-size:13px;font-weight:700;line-height:1.4;font-family:"Open Sans",Arial,sans-serif}

  /* centre */
  .brand{position:absolute;left:370px;top:20px;font-family:"Montserrat",Arial,sans-serif;font-weight:600;font-size:47px;letter-spacing:1px;color:var(--blue);white-space:nowrap}
  .tagline{position:absolute;right:392px;top:70px;font-family:"Open Sans",Arial,sans-serif;font-size:20px;color:var(--grey)}
  .benefits{position:absolute;left:400px;top:202px;list-style:none}
  .benefits li{width:196px;height:21px;margin-bottom:3px;background:var(--orange);border-radius:11px;text-align:center;font-family:"Open Sans",Arial,sans-serif;font-size:14.5px;line-height:21px;color:var(--ink)}
  .head-art{position:absolute;left:620px;top:148px;width:130px;height:200px}
  .count{position:absolute;left:526px;top:380px;width:120px;text-align:center;font-family:"Open Sans",Arial,sans-serif;font-size:19px;color:var(--grey)}
  .base-band{position:absolute;left:0;bottom:0;width:1200px;height:15px}

  /* facts panel */
  .facts{position:absolute;left:884px;top:26px;width:286px;border:2px solid var(--navy);padding:1px 5px 2px;font-size:9.6px;line-height:1.12}
  .facts h2{font-size:23px;font-weight:700;line-height:1.05;letter-spacing:.2px}
  .facts .serving{font-weight:700;font-size:10px;padding-bottom:2px;border-bottom:5px solid var(--navy)}
  .facts .head-row{font-size:7.5px;padding:2px 0 1px;border-bottom:1px solid var(--navy)}
  .facts table{width:100%;border-collapse:collapse}
  .facts td{padding:1px 0;vertical-align:top;border-bottom:1px solid var(--navy)}
  .facts td.amt{width:48px;text-align:left}
  .facts td.dv{width:10px;text-align:right}
  .facts tr:last-child td{border-bottom:4px solid var(--navy)}
  .facts .note{padding-top:1px}
  .panel-notes{position:absolute;left:884px;top:298px;width:292px;font-size:9.4px;line-height:1.15}
  .panel-notes b{font-weight:700}
  .panel-notes .caps{font-weight:700;margin-top:9px}
</style>
</head>
<body>
<div class="label">

  <section class="directions">
    <p><b>SUGGESTED USE:</b> 1 capsule taken 1 to 2 times daily preferably with meals or as directed by a healthcare professional.</p>
    <p><b>CAUTION:</b> Do not exceed recommended dose. St. John’s Wort may contribute to photosensitivity resulting in skin irritation and redness in persons exposed to strong sunlight or tanning booths. Avoid use in patients at risk of bleeding, taking anticoagulants, or with clotting disorders, based on case reports of bleeding. Discontinue use 2-3 weeks prior to some surgical and dental procedures due to increased risk of bleeding. Avoid use in couples who are trying to conceive, based on theoretical reduction of fertility. Pregnant or nursing mothers, children under 18, individuals with history of seizure, taking MAO inhibiting drugs, or with a known medical condition should consult a physician before using this or any dietary supplement. This product is manufactured and packaged in a facility which may also process milk, soy, wheat, egg, peanuts, tree nuts, fish and crustacean shellfish.</p>
  </section>

  <p class="fda-note">†These statements have not been evaluated by the Food &amp; Drug Administration. This product is not intended to diagnose, treat, cure or prevent any disease.</p>

  <p class="distributor">Distributed by:<br>Company Name<br>Full Address and Phone</p>

  <h1 class="brand">KELP VANTOR</h1>
  <p class="tagline">Brain Boost Supplement</p>

  <ul class="benefits">
    <li>Supports Focus</li>
    <li>Improves memory</li>
    <li>Promotes clear thinking</li>
  </ul>

  <svg class="head-art" role="img" aria-label="Illustration of a blue human head in profile with a glowing brain" viewBox="0 0 130 200">
    <defs>
      <radialGradient id="headGlow" cx="55%" cy="30%" r="70%">
        <stop offset="0" stop-color="var(--blue-light)"/>
        <stop offset="1" stop-color="var(--blue)"/>
      </radialGradient>
    </defs>
    <rect width="130" height="200" rx="12" fill="url(#headGlow)"/>
  </svg>

  <p class="count">30 capsules</p>

  <svg class="base-band" viewBox="0 0 1200 15" preserveAspectRatio="none" aria-hidden="true">
    <polygon points="0,0 570,0 555,15 0,15" fill="var(--orange)"/>
    <polygon points="570,0 1200,0 1200,15 555,15" fill="var(--blue)"/>
  </svg>

  <section class="facts">
    <h2>Supplement Facts</h2>
    <p class="serving">Serving Size 1 Capsule<br>Servings Per Container: 30</p>
    <p class="head-row">Amt Per Serv.&nbsp;&nbsp;%DV/RDI</p>
    <table>
      <tr><td><i>Ginkgo biloba</i> Leaf (24% extract)</td><td class="amt">50mg</td><td class="dv">*</td></tr>
      <tr><td>Phosphatidylserine 4% Complex<br>&nbsp;(consisting of Lecithin and Phosphatidylserine)</td><td class="amt">125mg</td><td class="dv">*</td></tr>
      <tr><td>N-Acetyl L-Carnitine HCl</td><td class="amt">50mg</td><td class="dv">*</td></tr>
      <tr><td>St. John’s Wort (0.3% extract)<br>&nbsp;(flower heads)</td><td class="amt">250mg</td><td class="dv">*</td></tr>
      <tr><td>L-Glutamine</td><td class="amt">150mg</td><td class="dv">*</td></tr>
      <tr><td><i>Bacopa monnieri</i> Leaf Extract<br>&nbsp;(20% bacosides)</td><td class="amt">120mg</td><td class="dv">*</td></tr>
      <tr><td>Vinpocetine (seeds)</td><td class="amt">2mg</td><td class="dv">*</td></tr>
      <tr><td>Huperzine-A (aerial plant)</td><td class="amt">10mcg</td><td class="dv">*</td></tr>
    </table>
    <p class="note">*Daily Value not established.</p>
  </section>

  <section class="panel-notes">
    <p><b>Other ingredients:</b> Gelatin (bovine), microcrystalline cellulose, vegetable magnesium stearate, and silicon dioxide.<br><b>ALLERGEN WARNING: CONTAINS SOY (LECITHIN).</b></p>
    <p class="caps">KEEP OUT OF THE REACH OF CHILDREN.<br>DO NOT USE IF SAFETY SEAL IS DAMAGED OR MISSING. STORE IN A COOL, DRY PLACE.</p>
  </section>

</div>
</body>
</html>
```